Business Card Design For A Renovation Contractor Company

We need a business card for a new company based in Singapore, our company name is "KT Planora". We are a renovation contractor that builds designs into reality. We build more of F&B restaurants, retail stores and commercial offices. We work very closely with designers. The final design should communicate to our client that we are a company that you can trust, that will plan and complete your project without giving you a headache. I like my client to remember my company as "KT". The beauty of SIMPLE is important.

Industry/Entity Type

Contractor

Requirements
Nice to have
• Black or Red base

```html
<!DOCTYPE html>
<html lang="en">
<head>
<meta charset="utf-8">
<title>KT Planora – Business Card</title>
<link rel="stylesheet" href="https://fonts.googleapis.com/css2?family=Tinos:wght@400;700&display=swap">
<style>
  :root {
    --card-grey: #636363;
    --ink: #0d0d0d;
    --brand-red: #e3131b;
    --mark-dark: #151515;
  }
  * { margin: 0; padding: 0; box-sizing: border-box; }
  html, body {
    width: 1200px;
    height: 720px;
    overflow: hidden;
    background: var(--card-grey);
  }
  .card {
    position: relative;
    width: 1200px;
    height: 720px;
    background: var(--card-grey);
    font-family: "Tinos", "Times New Roman", serif;
    color: var(--ink);
  }
  .brand {
    position: absolute;
    left: 0;
    top: 110px;
    width: 1200px;
    text-align: center;
  }
  .brand-dot {
    display: block;
    margin: 0 auto;
  }
  .brand-name {
    margin-top: 8px;
    font-size: 56px;
    font-weight: 400;
    line-height: 1;
    color: var(--brand-red);
  }
  .brand-rule {
    width: 312px;
    height: 1px;
    margin: 4px auto 0;
    background: var(--ink);
  }
  .brand-tagline {
    margin-top: 2px;
    font-size: 21px;
    line-height: 1;
    letter-spacing: 1px;
    color: var(--ink);
  }
  .person {
    position: absolute;
    left: 174px;
    top: 518px;
  }
  .person-name {
    font-size: 46px;
    line-height: 1;
    color: var(--brand-red);
    text-shadow: 0 0 3px rgba(0, 0, 0, 0.55);
  }
  .person-title {
    margin-top: 16px;
    margin-left: 2px;
    font-size: 15px;
    line-height: 1;
    letter-spacing: 24px;
  }
  .person-email {
    margin-top: 8px;
    margin-left: -4px;
    font-size: 33px;
    line-height: 1.1;
  }
  .divider {
    position: absolute;
    left: 590px;
    top: 517px;
  }
  .address {
    position: absolute;
    left: 674px;
    top: 504px;
    list-style: none;
    font-size: 26px;
    line-height: 51px;
    text-transform: uppercase;
  }
</style>
</head>
<body>
  <main class="card">
    <header class="brand">
      <svg class="brand-dot" width="106" height="106" viewBox="0 0 106 106" aria-hidden="true">
        <circle cx="53" cy="53" r="50" fill="var(--mark-dark)"/>
      </svg>
      <div class="brand-name">KT Planora</div>
      <div class="brand-rule"></div>
      <div class="brand-tagline">from careful plan to finish</div>
    </header>

    <section class="person">
      <div class="person-name">Marcus Tan.</div>
      <div class="person-title">DIRECTOR</div>
      <div class="person-email">Marcus@ktplanora.com</div>
    </section>

    <svg class="divider" width="8" height="128" viewBox="0 0 8 128" aria-hidden="true">
      <rect x="1.5" y="0" width="5" height="128" rx="2" fill="var(--brand-red)"/>
    </svg>

    <ul class="address">
      <li>8 Kembangan Lane</li>
      <li>#03-208 Kembangan Centre</li>
      <li>Singapore 415002</li>
    </ul>
  </main>
</body>
</html>
```